Physical Therapy Center for children Business Card

We need a Business Card for our company (Physical Therapy for children and youth with special needs) in Lisbon, Portugal. The name of the company is "Luz do Caminho"

The card must contain the following info:
- Logo: see uploaded file
- Name: Luz do Caminho
- Slogan: Semeamos Amor, colhemos sorrisos, distribuímos vitórias!
- Service: Terapias Especializadas
- Address: Rua Henrique Valente Morais 4B
- ZipCode: 2719-583 Póvoa de Santa Iria
- E-mail: geral@luzina.pt
- Site: www.luzina.pt
- Facebook: www.facebook.com/luzdocaminho
- Phone: +351 21 547 60 29
- Cell Phone: +351 96 718 45 93

The stationary should have contain all info from business card.

Target Market(s)

Parents of children with special needs

Industry/Entity Type

Physical Therapy

Contact Information for Business Card

The card design should be compatible with http://www.vellotype.com/product2/order_detail.php?gid=40

Requirements
Should not have
• The business card should not have a Black background. Use white or other color.

```html
<!DOCTYPE html>
<html lang="pt">
<head>
<meta charset="utf-8">
<title>Luz do Caminho — Cartão de Visita</title>
<link rel="stylesheet" href="https://fonts.googleapis.com/css2?family=Open+Sans:wght@400;600&display=swap">
<style>
  :root {
    --page-bg: #ecebea;
    --card-bg: #f6f4f3;
    --coral: #e86a62;
    --coral-deep: #e35d55;
    --slogan-red: #e2322b;
    --ink: #2f2f2f;
    --ink-soft: #444444;
    --on-coral: #ffffff;
    --teal: #3fb8a5;
  }
  * { box-sizing: border-box; margin: 0; padding: 0; }
  html, body {
    width: 1200px;
    height: 900px;
    overflow: hidden;
    background: var(--page-bg);
    font-family: "Open Sans", Arial, sans-serif;
  }
  .business-card {
    position: absolute;
    left: 112px;
    top: 150px;
    width: 975px;
    height: 600px;
    border-radius: 26px;
    background: var(--card-bg);
    overflow: hidden;
    box-shadow: 0 10px 30px rgba(0,0,0,0.12);
  }
  .contact-panel {
    position: absolute;
    inset: 0;
    width: 100%;
    height: 100%;
  }
  .brand {
    position: absolute;
    left: 54px;
    top: 218px;
    display: flex;
    align-items: center;
    gap: 16px;
  }
  .brand-dot {
    width: 26px;
    height: 26px;
    border-radius: 50%;
    background: var(--teal);
  }
  .brand-name {
    font-size: 46px;
    font-weight: 400;
    color: var(--ink);
    letter-spacing: -0.5px;
  }
  .slogan {
    position: absolute;
    left: 56px;
    top: 396px;
    font-size: 31px;
    line-height: 43px;
    font-weight: 600;
    color: var(--slogan-red);
  }
  .service {
    position: absolute;
    left: 56px;
    top: 520px;
    font-size: 23px;
    color: var(--ink-soft);
  }
  .contact-block {
    position: absolute;
    right: 50px;
    text-align: right;
    color: var(--on-coral);
    font-size: 25px;
    line-height: 36px;
  }
  .address { top: 98px; }
  .reach { top: 340px; }
  .social { top: 516px; }
  .contact-line {
    display: flex;
    justify-content: flex-end;
    align-items: center;
    gap: 8px;
  }
  .contact-icon {
    width: 18px;
    height: 18px;
    fill: var(--on-coral);
  }
</style>
</head>
<body>
  <article class="business-card">
    <svg class="contact-panel" viewBox="0 0 975 600" aria-hidden="true">
      <path d="M640 0 H975 V600 H590 C610 480 600 380 620 300 C640 200 600 90 640 0 Z" fill="var(--coral)" opacity="0.92"/>
    </svg>

    <div class="brand">
      <span class="brand-dot"></span>
      <span class="brand-name">Luz do Caminho</span>
    </div>

    <p class="slogan">Semeamos Amor, colhemos<br>sorrisos, distribuímos vitórias!</p>
    <p class="service">Terapias especializadas</p>

    <address class="contact-block address" style="font-style:normal">
      Rua Henrique<br>Valente Morais<br>4B 2719-583<br>Póvoa<br>de Santa Iria
    </address>

    <div class="contact-block reach">
      <div class="contact-line">+351 21 547 60 29
        <svg class="contact-icon" viewBox="0 0 20 20"><path d="M2 7c0-3 4-4 8-4s8 1 8 4v2h-4V7H6v2H2z M4 10h12l2 7H2z"/></svg>
      </div>
      <div class="contact-line">+351 96 718 45 93
        <svg class="contact-icon" viewBox="0 0 20 20"><path d="M6 1h8a1 1 0 0 1 1 1v16a1 1 0 0 1-1 1H6a1 1 0 0 1-1-1V2a1 1 0 0 1 1-1zm1 2v12h6V3z"/></svg>
      </div>
      <div class="contact-line">geral@luzina.pt
        <svg class="contact-icon" viewBox="0 0 20 20"><path d="M2 4h16v12H2z M3 5l7 6 7-6" stroke="var(--coral)" stroke-width="1.5"/></svg>
      </div>
      <div class="contact-line">www.luzina.pt
        <svg class="contact-icon" viewBox="0 0 20 20"><circle cx="10" cy="10" r="8"/><path d="M2 10h16M10 2c-4 4-4 12 0 16M10 2c4 4 4 12 0 16" stroke="var(--coral)" stroke-width="1.3" fill="none"/></svg>
      </div>
    </div>

    <div class="contact-block social">
      <div class="contact-line">luzdocaminho</div>
    </div>
  </article>
</body>
</html>
```